Property letting UK website

I need a web design for a new Property letting company in the UK. I already have a logo that was produced and won by a brief forge logo designer last week.

I like modern designs and require ease of functionality and usage. I already have a domain name registered so need to be able to link to that domain.

Regards,

Morven.

Target Market(s)

UK property

Industry/Entity Type

It Company

Number of Pages Required

5+ page

Requirements
Must have
• Home page, Current properties to let page, About us page, Contact us page, Testimonials page and ability to link to twitter and Facebook account.

```html
<!DOCTYPE html>
<html lang="en">
<head>
<meta charset="utf-8">
<title>Nestora – Residential Property Management</title>
<link href="https://fonts.googleapis.com/css2?family=Lato:wght@400;700&family=Merriweather:ital,wght@0,400;0,700;1,700&display=swap" rel="stylesheet">
<style>
:root{
  --black:#050505;
  --sky:#11a6e8;
  --navy:#0a3a72;
  --blue:#0f5ea8;
  --red:#c8231a;
  --ink:#333;
  --muted:#777;
  --paper:#f3f3f3;
  --footer:#262626;
  --footer-text:#ddd;
}
*{box-sizing:border-box;margin:0;padding:0}
html,body{width:849px;height:1200px;overflow:hidden;background:#fff}
body{position:relative;font-family:"Lato",sans-serif;color:var(--ink)}

/* header */
.site-header{position:absolute;left:0;top:0;width:849px;height:75px;background:var(--black)}
.brand{position:absolute;left:110px;top:20px;color:#fff;font-size:30px;font-weight:400;letter-spacing:1px;line-height:1}
.main-nav a{position:absolute;top:36px;font-size:9.5px;color:#fff;text-decoration:none}
.main-nav .active{left:312px;top:31px;width:59px;height:22px;border-radius:4px;background:var(--sky);text-align:center;line-height:22px}

/* hero */
.hero{position:absolute;left:0;top:75px;width:849px;height:371px}
.hero-photo{position:absolute;inset:0;background:linear-gradient(135deg,#a9cfe4 0%,#8a5a3c 28%,#b3b0a2 45%,#6d9a3e 70%,#3f7a2a 100%)}
.hero-arrow{position:absolute;top:180px;width:32px;height:32px;border-radius:50%;background:rgba(255,255,255,.6)}
.hero-dots{position:absolute;left:113px;top:354px}
.hero-dots span{display:inline-block;width:7px;height:7px;border-radius:50%;background:rgba(255,255,255,.6);margin-right:6px}
.tagline{position:absolute;left:380px;top:269px;width:375px;height:68px;background:rgba(20,20,20,.72);color:#fff;font-family:"Merriweather",serif;padding:10px 0 0 14px}
.tagline .l1{font-size:15px;line-height:22px}
.tagline .l2{font-size:17.5px;line-height:24px}

.quick-search{position:absolute;left:566px;top:6px;width:177px;height:233px;background:rgba(240,240,240,.93);border-radius:4px;font-size:8px}
.quick-search h2{position:absolute;left:14px;top:11px;font-weight:400;font-size:12.5px;color:var(--red)}
.select{position:absolute;height:14px;background:#fff;border:1px solid #bbb;padding-left:3px;line-height:12px;color:#333}
.select::after{content:"▾";position:absolute;right:3px;top:0}
.radio{position:absolute;top:66px;width:12px;height:12px;border-radius:50%;border:1px solid #999;background:#ddd}
.radio-label{position:absolute;top:67px;color:var(--red)}
.suburbs{position:absolute;left:19px;top:162px;width:140px;height:50px;background:#fff;border:1px solid #bbb;line-height:9.5px;padding-left:2px;overflow:hidden}
.suburbs div:first-child{background:#ddd}
.search-btn{position:absolute;left:99px;top:222px;width:59px;height:22px;border-radius:4px;background:var(--red);color:#fff;text-align:center;line-height:22px;font-size:9px}

/* services */
.services{position:absolute;left:0;top:446px;width:849px;height:208px;background:linear-gradient(180deg,var(--navy),var(--blue))}
.service{position:absolute;top:0;width:236px;text-align:center;color:#fff}
.service + .service{border-left:1px solid rgba(255,255,255,.12)}
.service-icon{position:absolute;left:78px;top:15px;width:80px;height:80px;border-radius:50%;background:#fff}
.service-icon svg{position:absolute;left:22px;top:22px}
.service h3{position:absolute;top:103px;width:100%;font-family:"Merriweather",serif;font-weight:400;font-size:13px}
.service p{position:absolute;top:124px;width:100%;font-size:10.5px;line-height:16px;font-weight:400}
.read-more{position:absolute;top:164px;left:85px;width:66px;height:17px;background:linear-gradient(#fff,#ccc);border:1px solid #999;color:var(--navy);font-family:"Merriweather",serif;font-style:italic;font-weight:700;font-size:9.5px;line-height:15px}

/* about */
.about-band{position:absolute;left:0;top:654px;width:849px;height:180px;background:var(--paper)}
.about-title{position:absolute;left:113px;top:670px;font-size:17px;font-weight:400;color:var(--sky)}
.about-title b{font-weight:400;font-size:21px}
.rule{position:absolute;height:0;border-top:1px dotted #aaa}
.about-text{position:absolute;left:110px;top:701px;width:422px;font-size:9.7px;line-height:14.9px;color:#444;text-align:justify}
.about-more{position:absolute;left:112px;top:799px;font-size:9.5px;color:var(--blue)}
.col-divider{position:absolute;left:552px;top:690px;width:1px;height:112px;background:#ddd}
.market-title{position:absolute;left:575px;top:669px;font-family:"Merriweather",serif;font-weight:400;font-size:18px;color:#222}
.market-title span{color:var(--blue)}
.market-item{position:absolute;left:575px;width:185px}
.market-item h4{font-weight:400;font-size:10px;color:#333}
.market-item p{font-size:8.5px;line-height:13px;color:var(--muted);margin-top:3px}

/* projects */
.projects-tab{position:absolute;left:335px;top:805px;width:198px;height:23px;background:linear-gradient(var(--blue),var(--navy));border-radius:0 0 40px 40px;color:#fff;font-weight:700;font-size:13px;text-align:center;line-height:22px}
.projects-strip{position:absolute;left:104px;top:847px;width:652px;height:125px;background:#f4f4f4;box-shadow:0 3px 5px rgba(0,0,0,.25)}
.project{position:absolute;top:12px;width:133px;height:100px;border:1px solid #bcd}
.project-caption{position:absolute;left:0;bottom:0;width:100%;height:25px;background:rgba(25,110,190,.85);color:#fff;padding:2px 0 0 8px;font-size:8px;line-height:10.5px}
.project-caption i{display:block}
.strip-arrow{position:absolute;top:55px;width:18px;height:18px;border-radius:50%;background:var(--navy)}
.strip-arrow svg{position:absolute;left:5px;top:5px}

/* footer */
.footer{color:var(--footer-text)}
.site-footer{position:absolute;left:0;top:983px;width:849px;height:217px;background:var(--footer)}
.footer-curve{position:absolute;left:0;top:965px}
.footer-brand{position:absolute;left:422px;top:1006px;color:#fff;font-size:24px}
.footer-h{position:absolute;top:1043px;font-weight:400;font-size:12px;color:#fff;padding-bottom:5px;border-bottom:1px dotted #555}
.quick-links a{position:absolute;left:94px;font-size:9.5px;color:var(--footer-text);text-decoration:none}
.quick-links a::before{content:"›";margin-right:5px}
.newsletter p{position:absolute;left:233px;top:1067px;width:160px;font-size:9.5px;line-height:13px;color:var(--footer-text)}
.email-input{position:absolute;left:233px;top:1102px;width:153px;height:19px;background:#fff;color:#888;font-size:9px;padding:4px 6px}
.subscribe{position:absolute;left:233px;top:1128px;width:73px;height:19px;background:#ddd;color:#333;font-weight:700;font-size:10px;text-align:center;line-height:19px}
.contact-line{position:absolute;left:439px;font-size:9.5px;line-height:13px;color:var(--footer-text)}
.contact-line.big{font-size:11px;font-weight:700;color:#fff}
.contact-icon{position:absolute;left:422px}
.map{position:absolute;left:578px;top:1068px;width:178px;height:89px;border:2px solid #fff;background:linear-gradient(135deg,#f3ecd8,#b8d4e8 45%,#e8dcc0 70%,#a9c9e3)}
.bottom-bar{position:absolute;left:0;top:1172px;width:849px;height:28px;border-top:1px solid #3a3a3a}
.follow{position:absolute;left:94px;top:1179px;font-size:12px;color:#fff}
.social{position:absolute;top:1178px;width:18px;height:18px;border-radius:50%;background:#5a6a7a}
.copyright{position:absolute;left:420px;top:1184px;font-size:9px;color:#fff}
</style>
</head>
<body>

<header class="site-header">
  <div class="brand">Nestora</div>
  <nav class="main-nav">
    <a class="active" href="#">Home</a>
    <a style="left:387px" href="#">Buy</a>
    <a style="left:419px" href="#">Sell</a>
    <a style="left:449px" href="#">Rent</a>
    <a style="left:484px" href="#">Testimonials</a>
    <a style="left:550px" href="#">About Us</a>
    <a style="left:604px" href="#">Services</a>
    <a style="left:654px" href="#">Contact Us</a>
  </nav>
</header>

<section class="hero">
  <div class="hero-photo" role="img" aria-label="Photo of modern brick apartment buildings with balconies and green trees"></div>
  <div class="hero-arrow" style="left:93px"></div>
  <div class="hero-arrow" style="left:725px">
    <svg width="32" height="32"><path d="M13 10l6 6-6 6" fill="none" stroke="#fff" stroke-width="2.5"/></svg>
  </div>
  <div class="hero-dots"><span></span><span></span><span></span></div>
  <div class="tagline">
    <div class="l1">WE ARE A RESIDENTIAL PROPERTY</div>
    <div class="l2">Management &amp; Consulting Company.</div>
  </div>

  <form class="quick-search">
    <h2>Quick Search</h2>
    <div class="select" style="left:19px;top:41px;width:140px">Residential Search</div>
    <div class="radio" style="left:29px"></div><div class="radio-label" style="left:46px">BUY</div>
    <div class="radio" style="left:71px"></div><div class="radio-label" style="left:88px">RENT</div>
    <div class="select" style="left:19px;top:96px;width:65px">Price Min</div>
    <div class="select" style="left:93px;top:96px;width:65px">Price Max</div>
    <div class="select" style="left:19px;top:123px;width:65px">Bedrooms</div>
    <div class="select" style="left:93px;top:123px;width:65px">Bathrooms</div>
    <div class="select" style="left:19px;top:148px;width:140px">All Types</div>
    <div class="suburbs">
      <div>All Suburbs</div><div>Abbey</div><div>Alfred Cove</div><div>Armadale</div><div>Attadale</div>
    </div>
    <div class="search-btn">Search</div>
  </form>
</section>

<section class="services">
  <div class="service" style="left:70px">
    <div class="service-icon">
      <svg width="36" height="36" viewBox="0 0 36 36"><path d="M6 30L24 12M12 30L30 12M8 8l20 20M28 8L8 28" stroke="#111" stroke-width="3.5" stroke-linecap="round"/></svg>
    </div>
    <h3>PROPERTY MANAGEMENT</h3>
    <p>Lorem ipsum dolor sit amet,<br>consectetuer adipiscing consequat.</p>
    <div class="read-more">Read More</div>
  </div>
  <div class="service" style="left:307px">
    <div class="service-icon">
      <svg width="36" height="36" viewBox="0 0 36 36"><path d="M4 16l10-8 8 4 10-4v10l-12 10-6-4-10-2z" fill="#111"/></svg>
    </div>
    <h3>PROPERTY CONSULTING</h3>
    <p>Lorem ipsum dolor sit amet,<br>consectetuer adipiscing consequat.</p>
    <div class="read-more">Read More</div>
  </div>
  <div class="service" style="left:544px">
    <div class="service-icon">
      <svg width="36" height="36" viewBox="0 0 36 36"><path d="M8 16L18 7l10 9v8H8z" fill="none" stroke="#111" stroke-width="3"/><path d="M3 28h22l8-6v6l-8 5H3z" fill="#111"/></svg>
    </div>
    <h3>OTHER SERVICES</h3>
    <p>Lorem ipsum dolor sit amet,<br>consectetuer adipiscing consequat.</p>
    <div class="read-more">Read More</div>
  </div>
</section>

<section class="about">
  <div class="about-band"></div>
  <h2 class="about-title">About <b>Nestora</b></h2>
  <div class="rule" style="left:113px;top:696px;width:420px"></div>
  <p class="about-text">Lorem ipsum dolor sit amet, consectetuer adipiscing elit, sed diam nonummy nibh nounl euismod tincidunt ut laoreet dolore magna aliquam erat volutpat. Ut wisi enim ad minim veniam, quisomol nostrud exerci tation ullamcorper suscipit lobortis nisl ut aliquip ex ea commodo consequat. Duis autem vel eum iriure dolor in hendrerit in vulputate velit esse molestie consequat, velillum dolore eu feugiat nulla facilisis at vero eros et accumsan et iusto odio dignissim qui blandit praesentedl luptatum zzril delenit augue duis dolore te feugait nulla facilisi.</p>
  <a class="about-more">Read more »</a>
  <div class="col-divider"></div>
  <h2 class="market-title">Market <span>Research</span></h2>
  <div class="rule" style="left:575px;top:696px;width:183px"></div>
  <div class="market-item" style="top:703px"><h4>Lorem ipsum 2013</h4><p>Lorem ipsum consel dolor sit amet, consectet uer adipiscing elit, sed diam</p></div>
  <div class="market-item" style="top:756px"><h4>Lorem ipsum 2014</h4><p>Lorem ipsum consel dolor sit amet, consectet uer adipiscing elit, sed diam</p></div>
</section>

<section class="projects">
  <div class="projects-strip">
    <div class="strip-arrow" style="left:11px"><svg width="8" height="8"><path d="M6 0L1 4l5 4z" fill="#fff"/></svg></div>
    <div class="project" style="left:38px;background:linear-gradient(#5d8fd0,#c9d3de 60%,#8a97a6)" role="img" aria-label="Photo of a modern office building">
      <div class="project-caption"><i>Project Name</i>Duis autem vel eum</div></div>
    <div class="project" style="left:185px;background:linear-gradient(#b9c9db,#9a5a3e 50%,#c9b79a)" role="img" aria-label="Photo of brick townhouses">
      <div class="project-caption"><i>Project Name</i>Duis autem vel eum</div></div>
    <div class="project" style="left:332px;background:linear-gradient(#9fc4e2,#c8a888 50%,#6d8a5a)" role="img" aria-label="Photo of a villa with palm trees">
      <div class="project-caption"><i>Project Name</i>Duis autem vel eum</div></div>
    <div class="project" style="left:479px;background:linear-gradient(#7f8a96,#d5d8dc 50%,#6f7780)" role="img" aria-label="Photo of city tower blocks">
      <div class="project-caption"><i>Project Name</i>Duis autem vel eum</div></div>
    <div class="strip-arrow" style="left:622px"><svg width="8" height="8"><path d="M2 0l5 4-5 4z" fill="#fff"/></svg></div>
  </div>
  <div class="projects-tab">Our Projects</div>
</section>

<footer class="footer">
  <div class="site-footer"></div>
  <svg class="footer-curve" width="849" height="70" viewBox="0 0 849 70">
    <path d="M80 18C200 55 330 40 420 18H0z" fill="#fff"/>
    <path d="M120 18C220 50 340 38 410 18C330 30 220 35 120 18z" fill="var(--blue)"/>
    <path d="M760 18C800 28 830 45 849 60V18z" fill="#fff"/>
    <path d="M765 18C805 30 832 46 849 66V58C830 42 805 28 780 18z" fill="#999"/>
  </svg>
  <div class="footer-brand">Nestora</div>

  <h3 class="footer-h" style="left:94px;width:106px">QUICK LINKS</h3>
  <nav class="quick-links">
    <a style="top:1067px">Home</a>
    <a style="top:1087px">About Us</a>
    <a style="top:1106px">Property Management</a>
    <a style="top:1126px">Property Consulting</a>
    <a style="top:1145px">Contact</a>
  </nav>

  <h3 class="footer-h" style="left:233px;width:155px">NEWSLETTER SIGNUP</h3>
  <div class="newsletter"><p>Stay connected and receive email updates from Nestora</p></div>
  <div class="email-input">Enter your email here</div>
  <div class="subscribe">SUBSCRIBE</div>

  <h3 class="footer-h" style="left:423px;width:120px">CONTACT DETAIL</h3>
  <svg class="contact-icon" style="top:1069px" width="11" height="15" viewBox="0 0 11 15"><path d="M5.5 0A5 5 0 0 0 .5 5c0 4 5 10 5 10s5-6 5-10a5 5 0 0 0-5-5z" fill="#fff"/><circle cx="5.5" cy="5" r="2" fill="var(--footer)"/></svg>
  <div class="contact-line" style="top:1067px">123 PG Duis aute irur dolore<br>srephenderit amit in voluptate</div>
  <svg class="contact-icon" style="top:1103px" width="11" height="11" viewBox="0 0 11 11"><path d="M2 0l2 3-1.2 1.3a7 7 0 0 0 3.9 3.9L8 7l3 2-1.5 2C4.5 11 0 6.5 0 1.5z" fill="#fff"/></svg>
  <div class="contact-line big" style="top:1101px">123 456 7890</div>
  <svg class="contact-icon" style="top:1125px" width="11" height="11" viewBox="0 0 11 11"><rect x="2" y="0" width="7" height="4" fill="#fff"/><rect x="0" y="4" width="11" height="5" fill="#fff"/><rect x="2" y="7" width="7" height="4" fill="#fff" stroke="var(--footer)"/></svg>
  <div class="contact-line big" style="top:1123px">123 456 7890</div>
  <svg class="contact-icon" style="top:1148px" width="11" height="8" viewBox="0 0 11 8"><rect width="11" height="8" fill="#fff"/><path d="M0 0l5.5 4.5L11 0" fill="none" stroke="var(--footer)"/></svg>
  <div class="contact-line" style="top:1145px">hello@nestora.co.uk</div>
  <div class="map" role="img" aria-label="Street map showing the office location"></div>

  <div class="bottom-bar"></div>
  <div class="follow">Follow Us :</div>
  <a class="social" style="left:159px" aria-label="Social profile one"></a>
  <a class="social" style="left:183px" aria-label="Social profile two"></a>
  <a class="social" style="left:207px" aria-label="Social profile three"></a>
  <a class="social" style="left:231px" aria-label="Social profile four"></a>
  <div class="copyright">Copyright © 2014 - www.nestora.co.uk &nbsp;- All rights reserved.</div>
</footer>

</body>
</html>
```